FUN Construction Open House Invitation

Open House for New Office of MVDP Construction, we have a logo, not sure what other graphics to put on the invitation and make it fun

Main target audience: Residential Building Architects (Custom Homes)
so we want to maybe target it towards that with a sketch of design/house/plans?
Drinks and food at: Verdel Cantina around the corner
LUCKY DOOR PRIZES: zentab, etc (need to be present to win)
Current BORING design attached
Event is on Thursday, 7/15 from 3-6 pm
Location: 718 Elmcrest, Suite 502-7 in Laguna Beach
Company: MVDP Construction (logo attached)
RSVP by 7/12 to office@mvdpbuild.example or 949-555-0172

Target Market(s)

Residential Building Architects for Custom Homes

Font styles to use
Other font styles liked:
• SOMETHING MODERN

Requirements
Must have
• Graphics, MODERN & FUN & ARTSY look but not too crowded
Should it be a charicature of the team? (with our english bulldog?)
A charicature of our english bulldog on a surfboard or skateboard or too cheesy?
Should not have
• Hammer or any other graphics like that, we are not a handyman company
High end custom home construction working with architects

```html
<!DOCTYPE html>
<html lang="en">
<head>
<meta charset="utf-8">
<title>MVDP Construction – Open House Invitation</title>
<link rel="stylesheet" href="https://fonts.googleapis.com/css2?family=Barlow:wght@400;500;600;700;800&family=Russo+One&display=swap">
<style>
  :root {
    --backdrop: #636363;
    --frame: #8c8c8c;
    --ink: #000000;
    --white: #ffffff;
    --orange: #f07a14;
  }
  * { box-sizing: border-box; margin: 0; padding: 0; }
  html, body {
    width: 989px; height: 1200px; overflow: hidden;
    background: var(--backdrop);
  }
  .invite {
    position: absolute; left: 24px; top: 275px;
    width: 940px; height: 650px;
    background: var(--frame);
    padding: 18px;
  }
  .invite__face {
    position: relative; width: 100%; height: 100%;
    background: var(--ink); color: var(--white);
    font-family: "Barlow", sans-serif;
  }
  .headline {
    position: absolute; left: 0; right: 0; top: 34px;
    text-align: center; font-family: "Russo One", sans-serif;
    font-size: 39px; line-height: 1.38; letter-spacing: 0.5px;
  }
  .headline__sub { color: var(--orange); display: block; }
  .when {
    position: absolute; left: 0; right: 0; top: 160px; height: 102px;
  }
  .when__day, .when__date, .when__time {
    position: absolute; font-weight: 800; font-size: 40px; line-height: 1.2;
  }
  .when__day { left: 70px; top: 30px; }
  .when__date { left: 370px; width: 200px; top: 4px; text-align: center; }
  .when__date sup { font-size: 22px; vertical-align: 16px; }
  .when__time { left: 630px; top: 22px; font-weight: 700; }
  .rule-dotted {
    position: absolute; top: 0; height: 100%;
    border-left: 3px dotted var(--orange);
  }
  .rule-dotted--a { left: 340px; }
  .rule-dotted--b { left: 598px; }
  .venue {
    position: absolute; left: 0; right: 0; top: 278px;
    text-align: center; font-size: 29px; font-weight: 600; line-height: 1.3;
  }
  .venue__lead { color: var(--orange); font-weight: 700; display: block; }
  .perk {
    position: absolute; top: 400px; display: flex; align-items: center; gap: 10px;
    font-size: 23px; line-height: 1.3;
  }
  .perk--food { left: 40px; font-weight: 600; }
  .perk--prize { left: 478px; }
  .perk__label { color: var(--orange); font-weight: 700; }
  .perk__note { font-weight: 400; }
  .perk__icon { width: 58px; height: 58px; flex: none; }
  .perks-divider {
    position: absolute; left: 455px; top: 402px; height: 72px;
    border-left: 3px dotted var(--white);
  }
  .rsvp {
    position: absolute; left: 40px; top: 508px;
    font-size: 25px; line-height: 1.22;
  }
  .rsvp__lead { color: var(--orange); font-weight: 700; }
  .rsvp__line { display: flex; align-items: center; gap: 8px; }
  .rsvp__or { color: var(--orange); font-weight: 600; }
  .rsvp__icon { width: 20px; height: 20px; flex: none; }
  .rsvp__web { margin-left: 16px; display: inline-flex; align-items: center; gap: 8px; }
  .brand {
    position: absolute; right: 48px; top: 535px;
    display: flex; align-items: center; gap: 12px;
    font-family: "Russo One", sans-serif; font-size: 27px; color: var(--orange);
  }
  .brand__mark { width: 24px; height: 24px; background: var(--orange); }
</style>
</head>
<body>
  <article class="invite">
    <div class="invite__face">
      <h1 class="headline">RESIDENTIAL BUILDING ARCHITECTS<span class="headline__sub">(CUSTOM HOMES)</span></h1>

      <section class="when">
        <div class="when__day">THURSDAY</div>
        <span class="rule-dotted rule-dotted--a"></span>
        <div class="when__date">JULY 15<sup>TH</sup><br>2021</div>
        <span class="rule-dotted rule-dotted--b"></span>
        <div class="when__time">3 pm - 6 pm</div>
      </section>

      <p class="venue"><span class="venue__lead">MVDP’s new office Location at</span>718 Elmcrest, Suite 502-7 in Laguna Beach</p>

      <div class="perk perk--food">
        <svg class="perk__icon" viewBox="0 0 58 58" fill="none" stroke="var(--orange)" stroke-width="3" stroke-linejoin="round" aria-hidden="true">
          <path d="M6 28 Q6 14 22 14 Q38 14 38 28 Z"/>
          <rect x="5" y="32" width="34" height="6" rx="3"/>
          <path d="M6 42 H38 V48 Q38 52 34 52 H10 Q6 52 6 48 Z"/>
          <path d="M40 18 H54 L51 54 H43 Z"/>
          <path d="M47 18 L50 6 H55"/>
        </svg>
        <div><span class="perk__label">DRINKS AND FOOD AT:</span><br>Verdel Cantina around the corner</div>
      </div>

      <span class="perks-divider"></span>

      <div class="perk perk--prize">
        <svg class="perk__icon" viewBox="0 0 58 58" fill="none" stroke="var(--orange)" stroke-width="3" stroke-linejoin="round" aria-hidden="true">
          <rect x="4" y="8" width="50" height="24" rx="2"/>
          <circle cx="29" cy="20" r="7"/>
          <path d="M20 30 V44 H38 V30"/>
          <path d="M16 52 H42"/>
        </svg>
        <div><span class="perk__label">LUCKY DOOR PRIZES:</span> <b>zentab, etc</b><br><span class="perk__note">(need to be present to win)</span></div>
      </div>

      <section class="rsvp">
        <div class="rsvp__lead">RSVP by 7/12 to</div>
        <div class="rsvp__line">
          <svg class="rsvp__icon" viewBox="0 0 20 20" aria-hidden="true"><rect x="1" y="4" width="18" height="12" rx="1" fill="var(--orange)"/><path d="M1 5 L10 11 L19 5" stroke="var(--ink)" stroke-width="2" fill="none"/></svg>
          <span>office@mvdpbuild.example <span class="rsvp__or">or</span></span>
        </div>
        <div class="rsvp__line">
          <svg class="rsvp__icon" viewBox="0 0 20 20" aria-hidden="true"><path d="M4 2 L8 2 L9 6 L7 8 Q9 12 12 13 L14 11 L18 12 L18 16 Q17 18 14 18 Q3 15 2 5 Q2 2 4 2 Z" fill="var(--orange)"/></svg>
          <span>949-555-0172</span>
          <span class="rsvp__web">
            <svg class="rsvp__icon" viewBox="0 0 20 20" fill="none" stroke="var(--orange)" stroke-width="2" aria-hidden="true"><circle cx="10" cy="10" r="8"/><ellipse cx="10" cy="10" rx="3.5" ry="8"/><path d="M2 10 H18"/></svg>
            www.mvdpbuild.example
          </span>
        </div>
      </section>

      <div class="brand"><span class="brand__mark"></span>MVDP Construction</div>
    </div>
  </article>
</body>
</html>
```